Creative flyer for small business IT services

We are an IT services company based in Western Australia. We're looking to expand our market share amongst small businesses and need a brochure/flyer designed to give them a good overview of why we can help them. The design and layout should be consistent with an existing company profile brochure (included) but please be creative. A comprehensive brief with copy and a rough layout is included.

Small Business

```html
<!DOCTYPE html>
<html lang="en">
<head>
<meta charset="utf-8">
<title>Blocklane – Small Business IT Solutions</title>
<link rel="stylesheet" href="https://fonts.googleapis.com/css2?family=Ubuntu:wght@300;400;500;700&display=swap">
<style>
  :root {
    --brand-red: #a81f2b;
    --ink: #2a2a2a;
    --ink-soft: #4a4a4a;
    --panel: #e6e6e6;
    --paper: #ffffff;
    --soil: #6b4a33;
    --leaf: #7cab3a;
  }
  * { margin: 0; padding: 0; box-sizing: border-box; }
  html, body { width: 873px; height: 1200px; overflow: hidden; background: var(--paper); }
  body { font-family: "Ubuntu", sans-serif; color: var(--ink); }
  .flyer { position: relative; width: 873px; height: 1200px; background: var(--paper); }
  .abs { position: absolute; }

  .masthead { left: 0; top: 0; width: 873px; height: 200px; background: var(--brand-red); }
  .masthead-title { left: 43px; top: 128px; font-weight: 300; font-size: 38px; color: #fff; letter-spacing: 0.2px; }
  .masthead-mark { left: 730px; top: 29px; width: 111px; height: 111px; background: #fff; }
  .masthead-name { left: 700px; top: 146px; width: 141px; text-align: right; font-weight: 300; font-size: 20px; color: #fff; }

  .hero-lead { left: 46px; top: 230px; font-size: 24px; font-weight: 700; }
  .hero-sub { left: 46px; top: 258px; font-size: 23px; font-weight: 300; }
  .hero-visual { left: 12px; top: 290px; width: 850px; height: 140px;
    background: linear-gradient(180deg, rgba(255,255,255,0) 0%, rgba(124,171,58,0.35) 45%, var(--soil) 100%); }
  .divider-band { left: 0; top: 437px; width: 873px; height: 12px; background: var(--brand-red); }

  .intro-heading { left: 43px; top: 473px; width: 470px; font-size: 23px; font-weight: 300; line-height: 30px; }
  .intro-body { left: 43px; top: 548px; width: 520px; font-size: 12.8px; font-weight: 300; line-height: 17.5px; }
  .intro-why { left: 43px; top: 629px; font-size: 12.8px; font-weight: 300; }
  .benefits { left: 43px; top: 650px; list-style: none; font-size: 12px; font-weight: 300; line-height: 15.5px; }
  .benefits li { padding-left: 13px; position: relative; }
  .benefits li::before { content: ""; position: absolute; left: 0; top: 5px; width: 6px; height: 6px;
    border: 1.6px solid var(--brand-red); border-radius: 50%; }

  .side-panel { background: var(--panel); left: 590px; width: 239px; padding: 12px 13px; font-weight: 300;
    font-size: 10.6px; line-height: 13.5px; color: var(--ink-soft); }
  .side-panel h3 { font-size: 14px; font-weight: 500; color: var(--ink); margin-bottom: 6px; }
  .side-panel p { margin-bottom: 7px; }
  .side-panel .cite { font-weight: 700; color: var(--ink); margin-bottom: 14px; }
  .audit { top: 480px; height: 168px; }
  .testimonials { top: 653px; height: 304px; }

  .service-head { top: 727px; height: 39px; background: var(--panel); font-size: 14px; font-weight: 300;
    display: flex; align-items: center; }
  .service-body { top: 771px; height: 186px; background: var(--panel); padding: 6px 14px 0; }
  .service-icon { width: 56px; height: 56px; margin: 0 auto 10px; border-radius: 8px; background: var(--brand-red); }
  .service-text { font-size: 10.4px; line-height: 11.2px; font-weight: 300; text-align: justify; text-align-last: center; color: var(--ink-soft); }
  .col-a { left: 43px; width: 181px; }
  .col-b { left: 230px; width: 170px; }
  .col-c { left: 406px; width: 178px; }
  .col-a.service-head { padding-left: 32px; }
  .col-b.service-head { padding-left: 14px; }
  .col-c.service-head { padding-left: 14px; }

  .partners-title { left: 46px; top: 972px; font-size: 13px; font-weight: 700; }
  .partners-text { left: 46px; top: 989px; width: 440px; font-size: 13px; font-weight: 300; line-height: 17.5px; }
  .badge { background: #d9d9d9; }
  .badge-a { left: 511px; top: 974px; width: 170px; height: 30px; background: #eaeaea; }
  .badge-b { left: 511px; top: 1011px; width: 115px; height: 44px; background: #1f3a55; }
  .badge-c { left: 638px; top: 988px; width: 70px; height: 70px; transform: rotate(45deg); background: #f0f2f4; }
  .badge-d { left: 716px; top: 984px; width: 115px; height: 84px; border-radius: 6px; background: #ececec; }
  .badge-d::before { content: ""; position: absolute; left: 15px; top: 12px; width: 95px; height: 14px; background: #e01f26; }

  .closing-line { left: 46px; top: 1087px; font-size: 12.8px; font-weight: 300; }
  .footer-brand { left: 46px; top: 1130px; display: flex; align-items: center; gap: 8px; font-size: 19px; font-weight: 300; }
  .footer-brand .mark { width: 32px; height: 32px; background: var(--brand-red); }
  .footer-rule { top: 1120px; width: 2px; height: 46px; background: var(--brand-red); }
  .footer-address { left: 245px; top: 1130px; width: 200px; text-align: center; font-size: 10.5px; font-weight: 300; line-height: 13.5px; }
  .footer-web { left: 452px; top: 1130px; width: 205px; text-align: center; font-size: 10.5px; font-weight: 300; line-height: 13.5px; }
  .footer-web strong { font-weight: 500; }
  .footer-phone { left: 690px; top: 1133px; width: 170px; text-align: center; font-size: 20px; font-weight: 500; }
  .base-band { left: 0; top: 1191px; width: 873px; height: 9px; background: var(--brand-red); }
</style>
</head>
<body>
<main class="flyer">
  <header class="abs masthead"></header>
  <h1 class="abs masthead-title">Small Business IT Solutions</h1>
  <div class="abs masthead-mark"></div>
  <div class="abs masthead-name">blocklane</div>

  <p class="abs hero-lead">Small business. Big ideas.</p>
  <p class="abs hero-sub">We’ll help your business grow.</p>
  <div class="abs hero-visual" role="img" aria-label="Row of seedlings in mounds of soil growing from small sprouts to a leafy plant"></div>
  <div class="abs divider-band"></div>

  <h2 class="abs intro-heading">We help small businesses get ahead of the pack.</h2>
  <p class="abs intro-body">You’ve always got more to do. In a small business, the last thing you need is another hat to wear. You shouldn’t need to become a computer engineer to keep your business running smoothly. Say goodbye to IT headaches<br>- our mission is to make your life easier.</p>
  <p class="abs intro-why">Here’s why small businesses love Blocklane:</p>
  <ul class="abs benefits">
    <li>We’re small business IT experts</li>
    <li>We speak plain English and won’t waste your time</li>
    <li>We care about our relationships</li>
    <li>We worry about IT so you don’t have to</li>
  </ul>

  <section class="abs side-panel audit">
    <h3>Audit</h3>
    <p>It helps to know where you stand.</p>
    <p>Get a clearer picture of your IT systems with our obligation-free IT audit and consultation.</p>
    <p>Contact us today and we’ll provide you with expert insights into how your business can benefit from today’s amazing technology.</p>
  </section>

  <section class="abs side-panel testimonials">
    <h3>Testimonials</h3>
    <p>Don’t just take our word for it! Here’s what some satisfied customers have to say about Blocklane:</p>
    <p>“We are pleased to have Blocklane as part of our team. I recommend Blocklane for any business seeking a trustworthy, reliable and effective IT service provider.”</p>
    <p class="cite">Tom Reyes, Coastline Imaging</p>
    <p>“Blocklane’s expertise has allowed us to test, analyse and improve the reliability and performance of our application, further improving the health and financial status of our business.”</p>
    <p class="cite">Lena Hart, Gradebook Pty Ltd</p>
  </section>

  <div class="abs service-head col-a">Support Services</div>
  <div class="abs service-head col-b">Monitoring &amp; Backup</div>
  <div class="abs service-head col-c">Hardware &amp; Software</div>

  <div class="abs service-body col-a">
    <div class="service-icon" role="img" aria-label="Red icon of a helper lifting a person over a wall"></div>
    <p class="service-text">If you run into a problem or need something done, just contact our Service Desk. Whether you have a single computer or a big team with complex requirements, our expert team can assist. We’ll give you an entire IT department for a fraction of the cost.</p>
  </div>
  <div class="abs service-body col-b">
    <div class="service-icon" role="img" aria-label="Red icon of a clock with a restore arrow"></div>
    <p class="service-text">Our Monitor &amp; Protect solution keep you safe from physical threats like theft, fire and floods, but also from electronic threats like viruses and hackers. Best of all - it happens automatically, so you can relax.</p>
  </div>
  <div class="abs service-body col-c">
    <div class="service-icon" role="img" aria-label="Red icon of a crossed spanner and screwdriver"></div>
    <p class="service-text">From a single keyboard to an entire infrastructure, we always take the time to help you select the right products. We supply world class hardware and software products from Helix, Orbis, Meridian, Pomelo, Cirrus,</p>
  </div>

  <h3 class="abs partners-title">World Class Partnerships</h3>
  <p class="abs partners-text">We proudly work with a range of industry leaders to ensure your business is powered by the best of today’s technology. With major partners including Meridian, Orbis, Cirrus, Vantage and Tidal Micro, you can be confident that our solutions are built on a strong foundation.</p>
  <div class="abs badge badge-a" aria-hidden="true"></div>
  <div class="abs badge badge-b" aria-hidden="true"></div>
  <div class="abs badge badge-c" aria-hidden="true"></div>
  <div class="abs badge badge-d" aria-hidden="true"></div>

  <p class="abs closing-line">Our valued customers are already enjoying the benefits of partnering with Blocklane. Join them by contacting us today:</p>

  <footer>
    <div class="abs footer-brand"><span class="mark"></span><span>blocklane</span></div>
    <div class="abs footer-rule" style="left:217px"></div>
    <address class="abs footer-address" style="font-style:normal">Level 12, 80 Harbour Street<br>Perth WA 6000</address>
    <div class="abs footer-rule" style="left:436px"></div>
    <div class="abs footer-web">sales@blocklane.example.au<br><strong>www.blocklane.example.au</strong></div>
    <div class="abs footer-rule" style="left:648px"></div>
    <div class="abs footer-phone">1300 555 018</div>
  </footer>
  <div class="abs base-band"></div>
</main>
</body>
</html>
```